Business Card Design

Our Motto is "Protecting Australia's Underground Utilities"

We want the Southern Cross inside a shield I have attached the southern cross and our old shield design

Product description is: Vacuum Excavation & Utility Location
Wet & Dry Vacuum Loading
Confined Space Entry Specialists
High Pressure Cleaning

The Southern Cross in the shield must be blue and white. The Company name must be Coastal Pipeguard Services. The Green & Gold Shield logo I uploaded is my OLD logo design. Thank you

Target Market(s)

Civil Construction

Industry/Entity Type

Business

Contact Information for Business Card

Coastal Pipeguard Services Pty Ltd
Corey Halbrook(Director)
0413862975
coreyh@pipeguardco.com.au
A.B.N.52938470116

Colors
0456a3

Requirements
Must have
• Southern Cross inside a shield, Blue and white design on the Southern Cross shield.
Must say Coastal Pipeguard Services P/L

```html
<!DOCTYPE html>
<html lang="en">
<head>
<meta charset="utf-8">
<title>Coastal Pipeguard Services – Business Card</title>
<link rel="stylesheet" href="https://fonts.googleapis.com/css2?family=Sorts+Mill+Goudy&family=Lato:wght@400&display=swap">
<style>
  :root {
    --backdrop: #4a4a4a;
    --card-white: #ffffff;
    --navy: #05003d;
    --ink-black: #111111;
    --service-lilac: #b3b0dc;
    --contact-purple: #4d4878;
    --card-edge: #222222;
    --mark-blue: #0456a3;
  }
  * { margin: 0; padding: 0; box-sizing: border-box; }
  html, body {
    width: 1200px;
    height: 961px;
    overflow: hidden;
    background: var(--backdrop);
  }
  .canvas {
    position: relative;
    width: 1200px;
    height: 961px;
  }
  .card {
    position: absolute;
    top: 55px;
    width: 474px;
    height: 809px;
    background: var(--card-white);
    text-align: center;
  }
  .card--front { left: 60px; }
  .card--back {
    left: 646px;
    border: 1px solid var(--card-edge);
  }

  /* Front */
  .brand-mark {
    position: absolute;
    left: 50%;
    top: 112px;
    width: 120px;
    height: 120px;
    margin-left: -60px;
    border-radius: 50%;
    background: var(--mark-blue);
  }
  .company-name {
    position: absolute;
    left: 0;
    right: 0;
    top: 285px;
    font-family: "Sorts Mill Goudy", "Times New Roman", serif;
    font-weight: 400;
    font-size: 40px;
    line-height: 40px;
    letter-spacing: 2px;
    color: var(--ink-black);
    text-transform: uppercase;
  }
  .services-band {
    position: absolute;
    left: 0;
    right: 0;
    bottom: 0;
    height: 309px;
    background: var(--navy);
    padding-top: 32px;
  }
  .service {
    font-family: "Lato", Arial, sans-serif;
    font-size: 19.5px;
    line-height: 25px;
    letter-spacing: 0.5px;
    color: var(--service-lilac);
    text-transform: uppercase;
    margin-bottom: 12px;
  }

  /* Back */
  .contact-name {
    position: absolute;
    left: 0;
    right: 0;
    top: 211px;
    font-family: "Sorts Mill Goudy", "Times New Roman", serif;
    font-size: 38px;
    line-height: 44px;
    letter-spacing: 0.5px;
    color: var(--contact-purple);
  }
  .contact-role {
    position: absolute;
    left: 0;
    right: 0;
    top: 254px;
    font-family: "Sorts Mill Goudy", "Times New Roman", serif;
    font-size: 23px;
    line-height: 26px;
    color: var(--contact-purple);
  }
  .contact-details {
    position: absolute;
    left: 0;
    right: 0;
    top: 616px;
    font-family: "Sorts Mill Goudy", "Times New Roman", serif;
    color: var(--contact-purple);
  }
  .contact-phone {
    font-size: 31px;
    line-height: 40px;
    letter-spacing: 1px;
  }
  .contact-email {
    font-size: 23px;
    line-height: 36px;
    margin-top: 2px;
  }
  .contact-abn {
    font-size: 17px;
    line-height: 28px;
    margin-top: 4px;
  }
</style>
</head>
<body>
  <main class="canvas">
    <section class="card card--front" aria-label="Card front">
      <span class="brand-mark" aria-hidden="true"></span>
      <h1 class="company-name">Coastal<br>Pipeguard<br>Services</h1>
      <div class="services-band">
        <p class="service">Vacuum Excavation<br>&amp; Utility Location</p>
        <p class="service">Wet &amp; Dry<br>Vacuum Loading</p>
        <p class="service">High Pressure<br>Cleaning</p>
        <p class="service">Confined Space Entry<br>Specialists</p>
      </div>
    </section>

    <section class="card card--back" aria-label="Card back">
      <h2 class="contact-name">Corey Halbrook</h2>
      <p class="contact-role">Director</p>
      <div class="contact-details">
        <p class="contact-phone">0413862975</p>
        <p class="contact-email">coreyh@pipeguardco.com.au</p>
        <p class="contact-abn">A.B.N.52938470116</p>
      </div>
    </section>
  </main>
</body>
</html>
```